Website for a Psychologist in Private Practice

I need a cool web design for my website: www.drvalporte.com. I would like it to look professional. Keep all the current content and add: Space for video; radio spots (see Silver Harbor Tunes Logo below for those); Quick Inquiry; Chatterbook link; 5 star rating on Rivo; a map; reviews from former patients. I am open to suggestions.

Target Market(s)

Those seeking individual and marital counseling.

Industry/Entity Type

Mental Health

Number of Pages Required

1 page

Font styles to use
Sans Serif
Other font styles liked:
• I'm open but no hard to read script

Requirements
Must have
• All the content on my home page with link for video and radio spots. List services and degrees and expertices (pics not necessary).
Nice to have
• A video of me and radio conversations (logo of Silver Harbor Tunes radio attached).
Should not have
• Cartoons, comedy, etc.... I don't need pictures of services (marital, depression, etc...) Just list those.

```html
<!DOCTYPE html>
<html lang="en">
<head>
<meta charset="utf-8">
<title>Dr. Lena M. Valporte — Clinical Psychologist</title>
<link rel="stylesheet" href="https://fonts.googleapis.com/css2?family=Open+Sans:ital,wght@0,400;0,600;0,700;1,400;1,600&display=swap">
<style>
:root{
  --blue:#2a7fc0;
  --blue-soft:#6aaedb;
  --ink:#2f3b45;
  --text:#7a8590;
  --line:#e2e6ea;
  --white:#ffffff;
  --footer-deep:#111b26;
  --pink:#dba5c0;
  --slate:#a6b3cf;
  --green:#a8c994;
  --mustard:#d8cb7e;
  --orange:#f2561e;
}
*{box-sizing:border-box;margin:0;padding:0}
html,body{width:1200px;height:2715px;overflow:hidden}
body{position:relative;background:var(--white);font-family:"Open Sans",Arial,sans-serif;color:var(--text)}
.abs{position:absolute}

/* header */
.site-header{left:0;top:0;width:1200px;height:74px;background:var(--white)}
.brand{left:194px;top:14px}
.brand-name{font-size:25px;font-weight:600;color:var(--blue);line-height:28px}
.brand-sub{font-size:11px;font-weight:600;color:var(--blue);letter-spacing:.3px}
.main-nav{right:176px;top:28px;display:flex;gap:22px;align-items:center;font-size:11.5px;color:var(--ink)}
.main-nav .active{color:var(--blue)}
.nav-social{font-size:11px;color:var(--blue);font-weight:700}
.nav-search{width:20px;height:20px;background:var(--blue);display:flex;align-items:center;justify-content:center}

/* hero */
.hero{left:0;top:74px;width:1200px;height:346px;background:radial-gradient(circle at 15% 25%,#e4efc2 0,#8fb34f 18%,#3f6d22 45%,#27481a 70%,#1c3714 100%)}
.hero-portrait{left:330px;top:0;width:380px;height:346px;background:linear-gradient(180deg,#d8c49a 0,#c9a88a 45%,#3a6ba0 75%,#2b5f95 100%);opacity:.55}
.hero-copy{left:700px;top:104px;width:330px;color:var(--white)}
.hero-title{font-size:28px;font-weight:400;letter-spacing:.5px}
.hero-quote{font-size:13px;font-style:italic;font-weight:600;line-height:17px;margin-top:8px}
.hero-degrees{list-style:none;font-size:11.5px;line-height:19px;margin-top:18px}

/* consultation */
.consult{left:0;top:420px;width:1200px;height:95px;background:var(--blue-soft)}
.consult-title{left:180px;top:20px;font-size:20px;font-weight:400;color:var(--white);letter-spacing:.3px}
.consult-text{left:180px;top:52px;font-size:12.5px;color:#e8f3fb}
.consult-btn{left:849px;top:29px;width:147px;height:36px;background:var(--white);color:var(--blue);font-size:12px;font-weight:600;display:flex;align-items:center;justify-content:center}

/* services */
.service{top:556px;width:265px}
.service-head{display:flex;align-items:center;gap:10px;font-size:12px;font-weight:700;color:var(--ink)}
.service-icon{width:16px;height:16px;border-radius:50%;background:var(--blue)}
.service-text{font-size:12px;line-height:17px;margin-top:18px}
.rule{height:1px;background:var(--line)}

/* section heading */
.heading{font-size:19px;color:var(--ink);letter-spacing:.6px;font-weight:400}
.heading-rule{height:1px;background:var(--line)}
.heading-rule::before{content:"";position:absolute;left:20px;top:-1px;width:30px;height:3px;background:var(--blue)}
.heading-rule.centered::before{left:50%;margin-left:-15px}

/* about */
.about-copy{left:183px;top:794px;width:542px;font-size:11.6px;line-height:17.8px}
.about-copy p{margin-bottom:17px}
.tile{width:114px;height:114px;color:var(--white);display:flex;flex-direction:column;align-items:center;justify-content:flex-end;padding-bottom:12px;font-size:12px;letter-spacing:.5px}
.tile svg{margin-bottom:14px}

/* media band */
.media{left:0;top:1125px;width:1200px;height:390px;background:linear-gradient(180deg,#7c9dbb 0,#a9c3d9 30%,#c8d9e6 55%,#8fa9c2 75%,#6c89a6 100%)}
.player{width:408px;height:100px;background:var(--white);border-radius:3px;box-shadow:0 1px 3px rgba(0,0,0,.2)}
.player-art{left:2px;top:2px;width:96px;height:96px;background:linear-gradient(135deg,#e04a7e,#4a79b6)}
.player-play{left:108px;top:10px;width:30px;height:30px;border-radius:50%;background:var(--orange)}
.player-title{left:146px;top:10px;font-size:10px;line-height:13px;color:#555}
.player-title b{color:#222;font-weight:600}
.player-btns{right:10px;top:10px;display:flex;gap:4px}
.player-btns span{border:1px solid #ddd;font-size:9px;padding:1px 6px;color:#333}
.wave{left:108px;top:44px;width:290px;height:32px;background:repeating-linear-gradient(90deg,#9a9a9a 0 2px,transparent 2px 3px);clip-path:polygon(0 55%,5% 35%,10% 50%,15% 20%,20% 45%,25% 25%,30% 40%,35% 10%,40% 35%,45% 20%,50% 45%,55% 15%,60% 40%,65% 30%,70% 50%,75% 20%,80% 40%,85% 30%,90% 50%,95% 35%,100% 45%,100% 100%,0 100%)}
.player-meta{left:108px;top:82px;font-size:8.5px;color:#999}
.player-brand{right:10px;top:82px;font-size:8px;color:#999;font-weight:600}
.video{left:617px;top:1245px;width:398px;height:226px;background:linear-gradient(180deg,#5f6e55 0,#7c8d6d 40%,#4b5a46 100%)}
.video-bar{left:617px;top:1449px;width:398px;height:22px;background:#1b1b1b;font-size:8px;color:#ccc;display:flex;align-items:center;padding-left:30px}

/* reviews */
.review-card{top:1638px;width:272px;height:114px;border:1px solid var(--line);padding:14px 16px;font-size:12px;font-style:italic;line-height:18px;color:#555;text-align:justify}
.avatar{top:1770px;width:62px;height:62px;border-radius:50%;background:linear-gradient(180deg,#c9b7a4,#8fa3b5);border:3px solid #eef1f4}
.reviewer{top:1788px;font-size:9px;color:#555}
.reviewer b{display:block;font-weight:600;letter-spacing:.4px;margin-bottom:7px}
.arrow-btn{top:1604px;width:16px;height:16px;border:1px solid var(--line);font-size:9px;color:#999;display:flex;align-items:center;justify-content:center}

/* enquiry */
.enquiry{left:757px;top:1625px;width:269px;height:212px;background:#e8f0f8;border:1px solid #d5e1ec}
.enquiry-title{left:12px;top:12px;font-size:15px;color:var(--ink)}
.field{background:var(--white);border:1px solid #b9cde0;font-size:9.5px;font-style:italic;color:#999;padding:3px 6px}
.submit{left:9px;top:178px;width:64px;height:20px;background:#2a6fb0;color:var(--white);font-size:11px;display:flex;align-items:center;justify-content:center}

/* contact */
.contact-band{left:0;top:1991px;width:1200px;height:81px;background:var(--blue-soft);color:var(--white);font-size:15px}
.contact-item{top:0;height:81px;display:flex;align-items:center;gap:18px;line-height:22px}
.contact-sep{top:14px;width:1px;height:53px;background:rgba(255,255,255,.45)}
.map{left:0;top:2072px;width:1200px;height:326px;background:linear-gradient(135deg,#ece8df 0,#e6e2d8 50%,#e9e5dc 100%)}

/* footer */
.footer{left:0;top:2398px;width:1200px;height:267px;background:linear-gradient(180deg,#24374a 0,#1b2a38 100%)}
.foot-title{font-size:12.5px;color:var(--white)}
.post{font-size:11px;line-height:15px;color:#d7dee5}
.post small{display:block;font-size:10px;color:#8e9aa6;margin-top:3px}
.post small span{color:var(--blue-soft)}
.badge{height:40px}
.rating-name{left:610px;top:152px;font-size:22px;font-weight:700;color:var(--white);line-height:30px}
.social-box{left:773px;top:2447px;width:239px;height:170px;background:var(--white)}
.social-cover{left:0;top:0;width:239px;height:90px;background:linear-gradient(135deg,#7b6d60,#3f4a56)}
.social-name{left:60px;top:6px;font-size:11px;font-weight:600;color:var(--white);line-height:13px}
.social-thumb{left:6px;top:6px;width:48px;height:48px;background:#c7b3a2;border:2px solid var(--white)}
.social-btn{top:64px;height:16px;background:#f3f4f6;border:1px solid #ccc;font-size:9px;color:#333;padding:0 5px;display:flex;align-items:center}
.social-line{left:6px;top:100px;font-size:9px;color:#555}
.friends{left:6px;top:120px;display:flex;gap:3px}
.friends span{width:22px;height:22px;background:#c4bcb2}
.social-label{left:6px;top:150px;font-size:9px;color:#888}
.bottom-bar{left:0;top:2665px;width:1200px;height:50px;background:var(--footer-deep)}
.copyright{left:183px;top:18px;font-size:11px;color:#8e9aa6}
.chat{left:724px;top:19px;width:304px;height:31px;background:#1f74c0;color:var(--white);font-size:12px;display:flex;align-items:center;justify-content:space-between;padding:0 18px 0 20px;border-radius:3px 3px 0 0}
</style>
</head>
<body>

<header class="site-header abs">
  <div class="brand abs">
    <div class="brand-name">Dr. Lena M. Valporte</div>
    <div class="brand-sub">CLINICAL PSYCHOLOGIST &nbsp;California # PSY20581</div>
  </div>
  <nav class="main-nav abs">
    <span class="active">HOME</span><span>SESSIONS</span><span>RECOURSES</span><span>BIO</span><span>CONTACT</span>
    <span class="nav-social">C</span>
    <span class="nav-search"><svg width="11" height="11" viewBox="0 0 12 12"><circle cx="5" cy="5" r="3.6" fill="none" stroke="#fff" stroke-width="1.6"/><line x1="7.6" y1="7.6" x2="11" y2="11" stroke="#fff" stroke-width="1.8"/></svg></span>
  </nav>
</header>

<section class="hero abs" role="img" aria-label="Portrait of the psychologist outdoors against a soft green garden background">
  <div class="hero-portrait abs"></div>
  <div class="hero-copy abs">
    <h1 class="hero-title">DO NOT COMPROMISE</h1>
    <p class="hero-quote">"Experience separates good psychologists from others with fewer and more proficient sessions"</p>
    <ul class="hero-degrees">
      <li>Doctoral Degree in Clinical Psychology</li>
      <li>Masters Degree in Counseling Psychology</li>
      <li>Doctoral Internship, Coastal University Medical Center</li>
      <li>Masters Internship, Linden Clinic</li>
    </ul>
  </div>
</section>

<section class="consult abs">
  <h2 class="consult-title abs">Have any Problems. Get a Free Consultation</h2>
  <p class="consult-text abs">Quisque posuere bibendum suscipit. Nullam gravida lectus non dolor volutpat bibendum.</p>
  <div class="consult-btn abs">GET SUGGESTION</div>
</section>

<div class="service abs" style="left:180px">
  <div class="service-head"><span class="service-icon"></span>DEPRESSION &amp; ANXIETY ISSUES</div>
  <p class="service-text">Sed ut perspiciatis unde omnis iste natus error sit voluptatem accusantium doloremque laudantium, totam rem aperiam</p>
</div>
<div class="service abs" style="left:473px">
  <div class="service-head"><span class="service-icon" style="border-radius:3px"></span>PERSONALITY DISORDERS</div>
  <p class="service-text">Sed ut perspiciatis unde omnis iste natus error sit voluptatem accusantium doloremque laudantium, totam rem aperiam</p>
</div>
<div class="service abs" style="left:766px">
  <div class="service-head"><span class="service-icon"></span>LIFE MANAGEMENT</div>
  <p class="service-text">Sed ut perspiciatis unde omnis iste natus error sit voluptatem accusantium doloremque laudantium, totam rem aperiam</p>
</div>

<div class="rule abs" style="left:172px;top:681px;width:854px"></div>

<h2 class="heading abs" style="left:183px;top:718px">KNOW ABOUT ME</h2>
<div class="heading-rule abs" style="left:163px;top:764px;width:300px"></div>
<div class="about-copy abs">
  <p>I'm so glad you are here. Choosing to see a professional for issues in your life can be difficult but also possibly life changing. Many postpone seeking help because they believe doing so acknowledges failure on their part. Really? We seek the help of experts all the time (contractors, mechanics, chefs, etc...) and what is more important than your life? Consulting with a neutral party to act in your best interest can be time well spent. So if you are willing to take the time to invest in counseling, make sure that it is with someone that is worth your time.</p>
  <p>Choose a licensed psychologist with a doctoral degree (Ph.D. or PsyD.) - both have over 10 years of education in the field of psychology, extensive internships and comprehensive licensing exams. Others have far less education if any. Also, consider the therapist's approach to therapy. I use a straightforward approach (psychobabble available upon request) with brief, solution-oriented sessions.</p>
  <p>Experience also separates good psychologists from others with fewer and more proficient sessions. My 20+ years of professional experience and my life experience contributes to the empathetic perspective I use to relate to each person I see. I also believe it is the reason 90% of my practice is referral based and why many other psychologists in the area seek my services.</p>
</div>

<h2 class="heading abs" style="left:762px;top:718px">EXPERTISE</h2>
<div class="heading-rule abs" style="left:742px;top:764px;width:300px"></div>
<div class="tile abs" style="left:766px;top:802px;background:var(--pink)">
  <svg width="38" height="34" viewBox="0 0 38 34"><path d="M19 32 C4 21 2 14 2 9 A8 8 0 0 1 19 6 A8 8 0 0 1 36 9 C36 14 34 21 19 32Z" fill="#fff"/></svg>DATING</div>
<div class="tile abs" style="left:898px;top:802px;background:var(--slate)">
  <svg width="44" height="32" viewBox="0 0 44 32"><circle cx="15" cy="18" r="11" fill="none" stroke="#fff" stroke-width="3.5"/><circle cx="29" cy="18" r="11" fill="none" stroke="#fff" stroke-width="3.5"/></svg>MARRIAGE</div>
<div class="tile abs" style="left:766px;top:930px;background:var(--green)">
  <svg width="40" height="36" viewBox="0 0 40 36"><circle cx="11" cy="6" r="5" fill="#fff"/><rect x="5" y="13" width="12" height="22" rx="3" fill="#fff"/><circle cx="29" cy="6" r="5" fill="#fff"/><rect x="23" y="13" width="12" height="22" rx="3" fill="#fff"/><circle cx="20" cy="20" r="3" fill="#fff"/><rect x="17" y="25" width="6" height="10" rx="2" fill="#fff"/></svg>PARENTING</div>
<div class="tile abs" style="left:898px;top:930px;background:var(--mustard)">
  <svg width="40" height="34" viewBox="0 0 40 34"><rect x="14" y="2" width="12" height="8" fill="none" stroke="#fff" stroke-width="3"/><rect x="2" y="9" width="36" height="23" rx="2" fill="#fff"/><rect x="17" y="17" width="6" height="5" fill="#d8cb7e"/></svg>PROFESSIONAL</div>

<section class="media abs" role="img" aria-label="Soft sky and sea backdrop">
  <h2 class="heading abs" style="left:180px;top:48px">RADIO SPOTS</h2>
  <div class="heading-rule abs" style="left:160px;top:94px;width:300px;background:rgba(255,255,255,.5)"></div>
  <h2 class="heading abs" style="left:617px;top:48px">FEATURED VIDEO</h2>
  <div class="heading-rule abs" style="left:597px;top:94px;width:300px;background:rgba(255,255,255,.5)"></div>
</section>

<div class="player abs" style="left:180px;top:1245px">
  <div class="player-art abs" role="img" aria-label="Radio show cover art"></div>
  <div class="player-play abs"></div>
  <div class="player-title abs">Silver Harbor Tunes<br><b>Dr. Lena M. Valporte</b></div>
  <div class="player-btns abs"><span>♥ Like</span><span>Share</span></div>
  <div class="wave abs"></div>
  <div class="player-meta abs">▶ 271 &nbsp;♥ 19 &nbsp;↻ 5</div>
  <div class="player-brand abs">WAVECAST</div>
</div>
<div class="player abs" style="left:180px;top:1365px">
  <div class="player-art abs" role="img" aria-label="Radio show cover art"></div>
  <div class="player-play abs"></div>
  <div class="player-title abs">Silver Harbor Tunes<br><b>Dr. Lena M. Valporte</b></div>
  <div class="player-btns abs"><span>♥ Like</span><span>Share</span></div>
  <div class="wave abs"></div>
  <div class="player-meta abs">▶ 793 &nbsp;♥ 34 &nbsp;↻ 64</div>
  <div class="player-brand abs">WAVECAST</div>
</div>

<div class="video abs" role="img" aria-label="Video still of a woman under a clear umbrella in the rain"></div>
<div class="video-bar abs">00:00 / 01:58</div>

<h2 class="heading abs" style="left:180px;top:1549px">PATIENT'S REVIEW</h2>
<div class="heading-rule abs" style="left:160px;top:1596px;width:348px"></div>
<div class="arrow-btn abs" style="left:695px">‹</div>
<div class="arrow-btn abs" style="left:713px">›</div>

<div class="review-card abs" style="left:172px">"Lorem ipsum dolor sit amet, consectetur adipiscing elit, sed do eiusmod tempor incididunt ut labore et dolore magna aliqua. Ut enim ad minim veniam."</div>
<div class="review-card abs" style="left:463px">"Quis nostrud exercitation ullamco laboris nisi ut aliquip ex ea commodo consequat. Duis aute irure dolor in reprehenderit in voluptate velit esse."</div>
<div class="avatar abs" style="left:188px" role="img" aria-label="Reviewer photo"></div>
<div class="reviewer abs" style="left:275px"><b>NORA WHITFIELD</b>Housewife</div>
<div class="avatar abs" style="left:478px" role="img" aria-label="Reviewer photo"></div>
<div class="reviewer abs" style="left:567px"><b>OWEN CALDER</b>School Teacher</div>

<h2 class="heading abs" style="left:762px;top:1549px">QUICK ENQUIRY</h2>
<div class="heading-rule abs" style="left:742px;top:1596px;width:210px"></div>
<form class="enquiry abs">
  <div class="enquiry-title abs">Contact us for details</div>
  <div class="field abs" style="left:9px;top:46px;width:250px">Enter Name</div>
  <div class="field abs" style="left:9px;top:72px;width:122px">Enter Email id</div>
  <div class="field abs" style="left:137px;top:72px;width:122px">Subject</div>
  <div class="field abs" style="left:9px;top:98px;width:250px;height:76px">Enter Message</div>
  <div class="submit abs">SUBMIT</div>
</form>

<div class="rule abs" style="left:172px;top:1880px;width:854px"></div>
<h2 class="heading abs" style="left:0;top:1912px;width:1200px;text-align:center">CONTACT</h2>
<div class="heading-rule centered abs" style="left:455px;top:1958px;width:290px"></div>

<section class="contact-band abs">
  <div class="contact-item abs" style="left:190px">
    <svg width="12" height="18" viewBox="0 0 12 18"><path d="M6 0A6 6 0 0 0 0 6C0 11 6 18 6 18S12 11 12 6A6 6 0 0 0 6 0Z" fill="#fff"/><circle cx="6" cy="6" r="2.2" fill="#6aaedb"/></svg>
    <span>418 Wren Street, Suite 120<br>Harbor Point, CA 92601</span>
  </div>
  <div class="contact-sep abs" style="left:452px"></div>
  <div class="contact-item abs" style="left:482px">
    <svg width="16" height="12" viewBox="0 0 16 12"><rect width="16" height="12" fill="#fff"/><path d="M0 0L8 7L16 0" fill="none" stroke="#6aaedb" stroke-width="1.4"/></svg>
    <span>lv@drvalporte.com</span>
  </div>
  <div class="contact-sep abs" style="left:744px"></div>
  <div class="contact-item abs" style="left:777px">
    <svg width="14" height="14" viewBox="0 0 14 14"><path d="M3 0L5.5 3.5L4 5.5C5 7.5 6.5 9 8.5 10L10.5 8.5L14 11L12 14C6 13.5 0.5 8 0 2Z" fill="#fff"/></svg>
    <span>(555) 018 2240</span>
  </div>
</section>

<div class="map abs" role="img" aria-label="Street map showing the office location with a red pin"></div>

<footer class="footer abs">
  <div class="foot-title abs" style="left:180px;top:50px">Recent Posts</div>
  <div class="post abs" style="left:180px;top:84px;width:250px">Sed ut perspiciatis unde omnis iste natus error sit voluptatem accusantium<small>By <span>Admin</span>, 15 Apr 2016</small></div>
  <div class="abs" style="left:180px;top:148px;width:250px;height:1px;background:rgba(255,255,255,.12)"></div>
  <div class="post abs" style="left:180px;top:162px;width:250px">Sed ut perspiciatis unde omnis iste natus error sit voluptatem accusantium<small>By <span>Admin</span>, 15 Apr 2016</small></div>

  <div class="foot-title abs" style="left:472px;top:50px">A portion of all revenue is donated to</div>
  <div class="badge abs" style="left:466px;top:85px;width:84px;background:#fff"></div>
  <div class="badge abs" style="left:570px;top:85px;width:122px;background:#8a9a3a"></div>
  <div class="foot-title abs" style="left:472px;top:162px">5 star rating on Rivo</div>
  <div class="rating-name abs">Rivo</div>
</footer>

<div class="social-box abs">
  <div class="social-cover abs" role="img" aria-label="Page cover photo"></div>
  <div class="social-thumb abs" role="img" aria-label="Page profile photo"></div>
  <div class="social-name abs">Dr. Lena M. Valporte<br><span style="font-weight:400;font-size:9px">Public Figure</span></div>
  <div class="social-btn abs" style="left:60px">Like Page</div>
  <div class="social-btn abs" style="left:188px">Share</div>
  <div class="social-line abs">Be the first of your friends to like this</div>
  <div class="friends abs"><span></span><span></span><span></span><span></span><span></span><span></span><span></span></div>
  <div class="social-label abs">Chatterbook</div>
</div>

<div class="bottom-bar abs">
  <div class="copyright abs">Copyright©Dr. Lena M. Valporte 2016</div>
  <div class="chat abs"><span>Live Chat With Me</span><span>⌃</span></div>
</div>

</body>
</html>
```